Web Design with a Twist! Not cheap design

Please note that this project is ending at 5pm on Tuesday the 28th of September, Australian Western Standard Time!!

Please also note that this project has now been guaranteed!

This project involves three primary elements:
* Logo design;
* Web design - of additional pages and page elements to fit into a site that is already in design/development;
* Graphic design - various images used on the site.

The following materials are included for the project:
* Project requirements
* Company / Site name
* Company / Site description
* Wireframes for new pages / page elements
* Screenshots of existing designs and accompanying definition of constraints for new designs
* PSDs for existing site designs
* Technical requirements for designs
* Content (to guide designs)

Project Requirements:

* Logo design:
This is a new company / site, so we need a new logo. We want to see what you come up with here without giving too much direction that may restrict creativity. If desired, you may find possible guidance through considering the company name, company description, and the existing site designs. Please note that the current logo in the site is for placeholder purposes only.

* Web design:
We need the following pages (and features) to be designed for the site:
• Home page
• Advertise page
• How it works page
We’ve provided some wireframes for the pages, however we definitely don't want you to be guided by the layout/styling at all - the wireframes are only there to indicate the features that we require on each page only. So please ignore all aspects of the wireframes except for the indications of features and functionality.

* Graphic design:
We need various images to be designed throughout the site. These include:
• The image at the top of the ‘Home’ page – please note we will provide some direction on this asap
• The image at the top of the ‘Advertise’ page – please note we will provide some direction n this asap
• The image at the top of the ‘How it Works’ pages
• The images that accompany each of the left hand menu items on the ‘How it Works’ pages (the main images & thumbnails if that’s part of your design). Please note that these images need to be constructed to match the Headlines for each of the ‘What’, ‘Who’, ‘Where’, etc menu items. These Headlines (and some descriptive text) can be found in the Content section at the end of this brief.
• The map of Australia for the ‘Home’ page
• The images to accompany the pricing section of the ‘Advertise’ page
• The variations of the ‘Life in the search lane’ images that are used on the ‘Home’, ‘Advertise’, and ‘How it Works’ pages. Please note that if you want to use different imagery (or no imagery, dependent upon your design) for the Home and Advertise pages then this is your call.

Company Name:
TaskBloom

Company / Site description:
This site will provide a means for contractors ('advertisers') to easily specify and advertise their services, coupled with a means for employers (‘buyers’) to easily seek out and contact these people.
The site will cater for contractor-side advertisements only; job postings will not be accommodated (turning the traditional job advertisement model on its head).
In general, the functionality of the site is somewhat like a mashup of sites like crewvault.com and stayvane.com. The site will incorporate the following primary features of contractor profile display and search, company profile display, (and an availability calendar for v2 release).

Constraints for designs:
On some of the existing designs you will notice that a number of the elements of the site have already been designed. When constructing your designs, please work in accordance with the following constraints:

You have to keep:
• Colour scheme in the header
• Colour scheme in the top navigation buttons (including text colour and background colour)
• Colour scheme for the buttons like on the Register page

You can ignore:
• The existing placeholder logo
• Border, layout, and colour scheme for page elements (like the lines around and inside the register section on the Register page)
• Design of text fields
• Font colour scheme throughout the site – the orange and grey headlines and body text
• Design and colour scheme of the map of Australia
• The breadcrumbs (whether or not they appear, and their layout, styling, colour scheme etc)
• Dropdown styling (assuming you had to make some; currently not on any pages we’re asking you to do) like on the Browse Profession page
• Profile styling (for the home page featured profiles) like on the Browse Profession page
• Footer styling
• Anything else we haven’t explicitly asked you to keep

Technical requirements for design:
Any site designs in either Layered Photoshop files (PSD's) or Illustrator Drawings (AI). RGB Color. Must fit current site design, we work to 1024 wide screens. Usuable area is defined in site designs that are attached in the Photoshop documents; it's around 960px.
Logo work needs to be Illustrator Drawings (AI) and EPS. Need CMYK images for printing and RGB for screen. Logos must include any special fonts that are used as TTF or Open Type. Logos need Color, Monochrome, Reversed and both Tall and Wide usages.

Content for the 'How it Works' pages - this content should guide the images that appear on each page.
* What
Headline: TaskBloom brings contractors and employers together
Descriptive text: (turns the traditional job search model on its head)
* Who
Headline: TaskBloom is for highly skilled professionals and fast moving companies
Descriptive text:
* Where
Headline: Anywhere in Australia, TaskBloom is working by your side
Descriptive text:
* Why
Headline: There are more than 1 million reasons to love TaskBloom
Descriptive text: In Australia, there are 1 million people who work as contractors in their main job, and a further 100,000 people who are contractors in their second job. That’s a lot of contractors!
* When
Headline: TaskBloom is forming partnerships 24 hours a day
Descriptive text:
* How
Headline: Life in the search lane, with TaskBloom
Descriptive text: Advertise on TaskBloom now, and get your life in the search lane.

Remember
Just remember the wireframes we have submitted are just a guide – we want to see your creativity shine. And above all else - have fun!
Thank you.
Updates

Please note the deadline for this design competition 5pm on Tuesday the 28th of September, Australian Western Standard Time.

Just under 3 days away!

The deadline of the project will soon be updated to reflect this.

Hi Designers!

Just to be 100% clear about the deadline - the timer is currently showing 7 hours too many. In other words, the project will end 7 hours before the timer finishes.

I will send a notification if the timer starts to display the correct time. So until then, please remember that the deadline is earlier than it seems!

Thanks

Hi Designers,

A couple of really important points:

Firstly - if everyone could please stick to the theme that we provided in the Photoshop files that would be excellent. It is not possible for us to create a new theme. We're dealing with very tight deadlines, so please just provide designs that fit within the current theme.

Secondly, we were really hoping for more illustrations / graphics to be provided in the designs. We're not a fan of the stock photos of generic business people. So please send through designs that incorporate illustrations / graphics for any imagery.

Also just a reminder that this competition is still ending 7 hours earlier than the timer currently displays.

Thanks.

Target Market(s)

The ‘advertiser’ target market for the site is white collar professionals, in all types of industries. The site will be catering for premium contractors only. The site will be catering for both 'in person' contractors, as well as 'knowledge economy' contractors. The site will not be seeking to compete with gigmora.com, plixo.com, taskrune.com, or similar sites.

The advertiser target market will also encompass companies and labour hire agencies that have contractors in their workforce.

The ‘buyer’ target market will encompass employers, recruitment agents, and member-to-member hiring.

Industry/Entity Type

Contractor

Requirements
Must have
• As per overview
Nice to have
• As per overview
Should not have
• As per overview

```html
<!DOCTYPE html>
<html lang="en">
<head>
<meta charset="utf-8">
<title>TaskBloom — Home</title>
<link href="https://fonts.googleapis.com/css2?family=Arimo:wght@400;700&display=swap" rel="stylesheet">
<style>
  :root {
    --orange: #ff6a00;
    --orange-dark: #e65a00;
    --page: #f1f1f1;
    --header-top: #7e8893;
    --tab: #b7bcc2;
    --tab-active: #f3f3f3;
    --ink: #3f4a55;
    --slate: #5c6874;
    --muted: #777;
    --field: #9aa3ab;
    --panel: #dedede;
    --footer: #6b6b6b;
    --footer-dark: #3a3a3a;
    --white: #fff;
  }
  * { box-sizing: border-box; margin: 0; padding: 0; }
  html, body { width: 887px; height: 1200px; overflow: hidden; }
  body { position: relative; background: var(--page); font-family: "Arimo", Arial, sans-serif; color: var(--ink); }
  .abs { position: absolute; }
  .lines { white-space: nowrap; }

  .site-header { left: 0; top: 0; width: 887px; height: 84px;
    background: radial-gradient(ellipse at 45% 0%, #b9c0c7 0%, var(--header-top) 60%, #6f7983 100%); }
  .brand-tag { left: 112px; top: 0; width: 100px; height: 108px; background: var(--orange);
    clip-path: polygon(0 0,100% 0,100% 100%,90% 96%,80% 100%,70% 96%,60% 100%,50% 96%,40% 100%,30% 96%,20% 100%,10% 96%,0 100%);
    display: flex; align-items: center; justify-content: center; }
  .brand-name { color: var(--white); font-size: 17px; font-weight: 700; }
  .account-bar { left: 612px; top: 0; width: 157px; height: 22px; background: #1e1e1e; border-radius: 0 0 6px 6px;
    font-size: 9px; color: var(--white); display: flex; align-items: center; justify-content: center; gap: 7px; }
  .account-bar .login { color: var(--orange); }
  .main-nav a { position: absolute; top: 55px; height: 29px; background: var(--tab); color: var(--white);
    border-radius: 6px 6px 0 0; font-size: 13px; text-decoration: none; display: flex; align-items: center; justify-content: center; }
  .main-nav a.active { background: var(--tab-active); color: var(--ink); }

  .hero { left: 111px; top: 131px; width: 662px; height: 202px; background: var(--white); border-radius: 8px;
    box-shadow: 0 1px 4px rgba(0,0,0,.18); overflow: hidden; }
  .hero-art { left: 355px; top: 0; width: 307px; height: 202px; background: linear-gradient(90deg,#fff 0%,#e3e5e8 35%,#c9ccd1 100%); }
  .hero-title { left: 25px; top: 63px; font-size: 16px; font-weight: 400; color: #333; white-space: nowrap; z-index: 1; }
  .hero-title em, .section-title em { font-style: normal; color: var(--orange); }
  .hero-rule { left: 25px; top: 90px; width: 300px; height: 1px; background: #e2e2e2; }
  .hero-text { left: 31px; top: 100px; font-size: 9px; line-height: 13px; color: #444; }
  .btn-light { left: 125px; top: 148px; width: 102px; height: 25px; border: 1px solid #b9bba8; border-radius: 4px;
    background: linear-gradient(#f6f7ea,#d8dbc4); font-size: 10px; color: #333; display: flex; align-items: center; justify-content: center; }

  .region-map { left: 166px; top: 366px; width: 228px; height: 200px; border-radius: 30px 20px 40px 60px;
    background: linear-gradient(135deg,#f1b57a 0%,#e79548 55%,#d07a2e 100%); }
  .search-panel { left: 449px; top: 368px; width: 322px; height: 198px; background: var(--panel);
    border: 1px solid #cfcfcf; border-radius: 5px; }
  .panel-title { left: 22px; top: 18px; font-size: 16px; font-weight: 400; color: var(--slate); }
  .field-label { left: 23px; font-size: 12px; color: #444; }
  .field { left: 94px; width: 198px; height: 30px; background: var(--field); border-radius: 2px;
    font-size: 10px; font-style: italic; color: #e8ecef; padding-left: 12px; display: flex; align-items: center; }
  .field .caret { position: absolute; right: 8px; font-style: normal; color: #5b636b; font-size: 10px; }
  .btn-orange { width: 250px; height: 35px; background: linear-gradient(var(--orange),var(--orange-dark)); border-radius: 3px;
    box-shadow: 0 2px 3px rgba(0,0,0,.25); color: var(--white); font-size: 13px; display: flex; align-items: center; justify-content: center; }

  .section-rule { left: 124px; top: 595px; width: 650px; height: 4px;
    background: radial-gradient(ellipse at center, rgba(0,0,0,.22) 0%, rgba(0,0,0,0) 70%); }
  .section-title { font-size: 16px; font-weight: 400; color: var(--slate); }
  .about-frame { left: 131px; top: 672px; width: 290px; height: 107px; background: var(--white);
    border: 1px solid #d4d4d4; border-radius: 7px; box-shadow: 0 1px 3px rgba(0,0,0,.12); }
  .about-name { left: 14px; top: 42px; font-size: 18px; color: var(--orange); }
  .about-split { left: 139px; top: 14px; width: 1px; height: 78px; background: #ddd; }
  .about-art { left: 146px; top: 8px; width: 136px; height: 90px; border-radius: 4px;
    background: linear-gradient(#fafafa,#d9d9d9); }
  .about-text { left: 134px; top: 798px; font-size: 9px; line-height: 17px; color: var(--muted); }

  .how-card { left: 120px; top: 901px; width: 306px; height: 105px; border: 1px solid #b5b5b5; border-radius: 6px;
    background: linear-gradient(#f4f4f4,#d5d5d5); box-shadow: 0 1px 3px rgba(0,0,0,.2); }
  .how-title { left: 96px; top: 26px; font-size: 16px; color: var(--slate); }
  .how-rule { left: 96px; top: 51px; width: 180px; height: 1px; background: #9a9a9a; }
  .how-sub { left: 96px; top: 59px; font-size: 16px; color: var(--orange); }

  .column-rule { left: 452px; top: 671px; width: 1px; height: 333px; background: #d0d0d0; }
  .profile-photo { left: 475px; width: 70px; height: 70px; background: var(--white); border: 1px solid #d5d5d5;
    border-radius: 7px; padding: 5px; }
  .profile-photo span { display: block; width: 100%; height: 100%; border-radius: 3px;
    background: linear-gradient(#c9ced3,#7f8892); }
  .profile-info { left: 557px; font-size: 9px; line-height: 16.5px; color: var(--muted); white-space: nowrap; }
  .profile-name { color: var(--orange); font-size: 10px; }
  .profile-role { color: #666; font-size: 8.5px; }
  .profile-rule { left: 475px; width: 282px; height: 1px; background: #d8d8d8; }

  .site-footer { left: 0; top: 1039px; width: 887px; height: 118px; background: var(--footer); }
  .footer-col h4 { font-size: 12px; font-weight: 700; color: #a9a9a9; margin-bottom: 10px; }
  .footer-col li { list-style: none; font-size: 8.5px; color: #e4e4e4; line-height: 13px; }
  .footer-col li::before { content: "▸"; color: var(--orange); font-size: 7px; margin-right: 9px; }
  .footer-divider { top: 1062px; width: 1px; height: 73px; background: #7b7b7b; }
  .footer-brand { left: 600px; top: 1086px; font-size: 24px; color: var(--white); }
  .legal-bar { left: 0; top: 1157px; width: 887px; height: 43px; background: var(--footer-dark); }
  .copyright { right: 127px; top: 16px; font-size: 8px; color: #eee; }
</style>
</head>
<body>
  <header class="abs site-header"></header>
  <div class="abs brand-tag"><span class="brand-name">TaskBloom</span></div>
  <div class="abs account-bar"><span class="login">LOGIN</span><span>|</span><span>REGISTER NOW</span></div>
  <nav class="main-nav">
    <a class="active" href="#" style="left:298px;width:61px">Home</a>
    <a href="#" style="left:367px;width:60px">Find</a>
    <a href="#" style="left:435px;width:74px">Advertise</a>
    <a href="#" style="left:517px;width:95px">How it Works</a>
    <a href="#" style="left:620px;width:72px">Blog</a>
    <a href="#" style="left:698px;width:71px">Login</a>
  </nav>

  <section class="abs hero">
    <div class="abs hero-art" role="img" aria-label="Business people assembling large white puzzle pieces"></div>
    <h1 class="abs hero-title">We Bring <em>Contactor</em> and <em>Employer</em> Together</h1>
    <div class="abs hero-rule"></div>
    <p class="abs hero-text lines">Lorem ipsum dolor sit amet, consectetur adipiscing elit. Aenean ligula<br>justo, faucibus a imperdiet vitae, vestibulum at diam. Proin ac nulla<br>lorem, ac cursus lectus. In in est sed felis mattis</p>
    <div class="abs btn-light">Register Now</div>
  </section>

  <div class="abs region-map" role="img" aria-label="Map of Australia divided into states and territories in orange tones"></div>

  <section class="abs search-panel">
    <h2 class="abs panel-title">Find Highly Skilled Professional</h2>
    <span class="abs field-label" style="top:58px">Keywords</span>
    <div class="abs field" style="top:56px">Keywords</div>
    <span class="abs field-label" style="top:102px">State</span>
    <div class="abs field" style="top:100px">Pick A State<span class="caret">| ▼</span></div>
    <div class="abs btn-orange" style="left:34px;top:147px">Find Contractors</div>
  </section>

  <div class="abs section-rule"></div>

  <h2 class="abs section-title" style="left:124px;top:634px">About <em>TaskBloom</em></h2>
  <div class="abs about-frame">
    <span class="abs about-name">TaskBloom</span>
    <div class="abs about-split"></div>
    <div class="abs about-art" role="img" aria-label="Illustration of a group of figures with speech bubbles"></div>
  </div>
  <p class="abs about-text lines">Praesent ultrices felis nulla. Aenean euismod nisl eu augue facilisis eu<br>tristique justo hendrerit. Aliquam volutpat nunc libero. Donec sit amtet<br>augue est, at venenatis urna. Morbi sapien massa, porta sed porttitor et,<br>aliquet eget enim. Morbi sapien massa, porta sed porttitor e</p>

  <div class="abs how-card">
    <svg class="abs" style="left:28px;top:34px" width="50" height="38" viewBox="0 0 50 38" aria-hidden="true">
      <path d="M3 34 C6 18 16 13 30 13 V3 L47 19 L30 35 V25 C18 25 9 28 3 34 Z" fill="none" stroke="#6a6a6a" stroke-width="2.5" stroke-linejoin="round"/>
    </svg>
    <span class="abs how-title">How it Works</span>
    <div class="abs how-rule"></div>
    <span class="abs how-sub">Life In The Seach Lane</span>
  </div>

  <div class="abs column-rule"></div>

  <h2 class="abs section-title" style="left:476px;top:634px">Featured <em>Profile</em></h2>

  <div class="abs profile-photo" style="top:669px"><span role="img" aria-label="Portrait photo of a featured professional"></span></div>
  <p class="abs profile-info" style="top:675px"><span class="profile-name">Dorian Vell</span> <span class="profile-role">- Senior Web Developer</span><br>Praesent ultrices felis nulla. Aenean euismod nisl eu<br>augue facilisis eu tristique justo hendrerit. Aliquam</p>
  <div class="abs profile-rule" style="top:755px"></div>

  <div class="abs profile-photo" style="top:767px"><span role="img" aria-label="Portrait photo of a featured professional"></span></div>
  <p class="abs profile-info" style="top:774px"><span class="profile-name">Jana Sorrel</span><span class="profile-role"> - Senior Account Servicing</span><br>Praesent ultrices felis nulla. Aenean euismod nisl eu<br>augue facilisis eu tristique justo hendrerit. Aliquam</p>
  <div class="abs profile-rule" style="top:853px"></div>

  <div class="abs profile-photo" style="top:866px"><span role="img" aria-label="Portrait photo of a featured professional"></span></div>
  <p class="abs profile-info" style="top:872px"><span class="profile-name">Otis Crane</span> <span class="profile-role">- Chief Financial Officer</span><br>Praesent ultrices felis nulla. Aenean euismod nisl eu<br>augue facilisis eu tristique justo hendrerit. Aliquam</p>
  <div class="abs profile-rule" style="top:950px"></div>

  <div class="abs btn-orange" style="left:484px;top:969px">Find Contractors</div>

  <footer class="abs site-footer"></footer>
  <div class="abs footer-col" style="left:133px;top:1061px"><h4>The Service</h4><ul><li>About</li><li>Browse</li><li>Login</li></ul></div>
  <div class="abs footer-divider" style="left:226px"></div>
  <div class="abs footer-col" style="left:255px;top:1061px"><h4>Support</h4><ul><li>Contact Us</li><li>FAQ</li></ul></div>
  <div class="abs footer-divider" style="left:371px"></div>
  <div class="abs footer-col" style="left:398px;top:1061px"><h4>Legal</h4><ul><li>Privacy &amp; Policy</li><li>Terms &amp; Conditions</li></ul></div>
  <div class="abs footer-divider" style="left:530px"></div>
  <span class="abs footer-brand">TaskBloom</span>
  <div class="abs legal-bar"><span class="abs copyright">Copyright © 2008 - 2010 CrewNest. Copyright&nbsp; Al Right Reserved</span></div>
</body>
</html>
```